It's a new electrical company based in Newcastle NSW. I would like a logo between the two words "BRYN (insert logo) VOLT". I would like the logo to represent electrical and celtic style. For example I have seen a light bulb with a celtic pattern in the middle which looked very good. I would like it to be a white card, mainly black writing and quite basic not too much going on. But maybe have the logo partially red or green?

BRYN VOLT
Electrical Contractors
Domestic, commercial, fault finding, testing, re wires, switchboard upgrades
License No: 738421K
Fully Insured
Phone: 0431587720

```html
<!DOCTYPE html>
<html lang="en">
<head>
<meta charset="utf-8">
<title>Bryn Volt – Business Card</title>
<link href="https://fonts.googleapis.com/css2?family=Open+Sans:wght@400;600&display=swap" rel="stylesheet">
<style>
  :root {
    --page-bg: #e9e7e3;
    --card-white: #ffffff;
    --ink: #1f1f1f;
    --band-black: #111111;
    --band-text: #f2f2f2;
    --accent-green: #6cc04a;
    --braid-grey: #bdbdbd;
  }
  html, body {
    margin: 0;
    width: 1200px;
    height: 1023px;
    overflow: hidden;
    background: var(--page-bg);
    font-family: "Open Sans", Arial, sans-serif;
  }
  .card {
    position: absolute;
    left: 150px;
    top: 236px;
    width: 900px;
    height: 550px;
    background: var(--card-white);
    box-shadow: 0 6px 24px rgba(0,0,0,0.18);
    overflow: hidden;
  }
  .brand {
    position: absolute;
    top: 52px;
    left: 0;
    width: 100%;
    display: flex;
    justify-content: center;
    align-items: center;
    gap: 26px;
    color: var(--ink);
    font-weight: 600;
    font-size: 82px;
    letter-spacing: 8px;
    line-height: 1;
  }
  .brand-dot {
    width: 74px;
    height: 74px;
    border-radius: 50%;
    background: var(--accent-green);
  }
  .services {
    position: absolute;
    top: 196px;
    left: 80px;
    width: 740px;
    margin: 0;
    text-align: center;
    color: var(--ink);
    font-size: 23px;
    line-height: 1.3;
  }
  .braid-band {
    position: absolute;
    top: 338px;
    left: 0;
    width: 100%;
    height: 22px;
    background: linear-gradient(#ffffff, var(--braid-grey) 50%, #ffffff);
  }
  .contact-band {
    position: absolute;
    top: 360px;
    left: 0;
    width: 100%;
    height: 190px;
    background: var(--band-black);
    color: var(--band-text);
  }
  .holder {
    position: absolute;
    left: 66px;
    top: 52px;
    font-size: 25px;
    line-height: 1.3;
  }
  .holder-name {
    font-weight: 600;
    font-size: 32px;
    letter-spacing: 1px;
    margin-bottom: 2px;
  }
  .details {
    position: absolute;
    left: 530px;
    top: 50px;
    font-size: 25px;
    line-height: 1.3;
  }
  .detail-row {
    display: flex;
    align-items: center;
    gap: 10px;
  }
  .detail-icon {
    width: 22px;
    height: 22px;
    flex: none;
  }
  .licence { padding-left: 10px; }
</style>
</head>
<body>
  <div class="card">
    <div class="brand">
      <span>BRYN</span>
      <span class="brand-dot"></span>
      <span>VOLT</span>
    </div>
    <p class="services">All Domestic and Commercial electrical work undertaken including new installation, re wires, fault finding, testing, switchboard upgrades and more</p>

    <div class="braid-band" role="img" aria-label="Celtic braided border pattern"></div>

    <div class="contact-band">
      <div class="holder">
        <div class="holder-name">LIAM CARVER</div>
        <div>Certified Electrician</div>
        <div>Fully insured</div>
      </div>
      <div class="details">
        <div class="detail-row">
          <svg class="detail-icon" viewBox="0 0 24 24" aria-hidden="true">
            <circle cx="12" cy="12" r="12" fill="#f2f2f2"/>
            <path d="M8.2 6.5c.4-.4 1-.4 1.3 0l1.5 2c.3.4.2.9-.1 1.2l-.8.8c.6 1.3 1.7 2.4 3 3l.8-.8c.3-.3.8-.4 1.2-.1l2 1.5c.4.3.4.9 0 1.3l-1 1c-.6.6-1.5.8-2.3.4-2.9-1.3-5.2-3.6-6.5-6.5-.4-.8-.2-1.7.4-2.3z" fill="#111"/>
          </svg>
          <span>0431 587720</span>
        </div>
        <div class="detail-row">
          <svg class="detail-icon" viewBox="0 0 24 24" aria-hidden="true">
            <circle cx="12" cy="12" r="12" fill="#f2f2f2"/>
            <rect x="6" y="8" width="12" height="8.5" rx="1" fill="#111"/>
            <path d="M6.5 8.6 12 13l5.5-4.4" stroke="#f2f2f2" stroke-width="1.2" fill="none"/>
          </svg>
          <span>liam@brynvolt.com.au</span>
        </div>
        <div class="licence">License No:738421K</div>
      </div>
    </div>
  </div>
</body>
</html>
```